Business Card & Logo Design - Hedge Fund

We need a business card and logo design for a hedge fund. The hedge fund is named Morvane Equity LLC. Morvane Equity was created by finance professors and the strategy is based academic research that looks for patterns in stock prices. The design should look conservative, solid, strong. We favor a classic style - nothing flashy. The logo can relate to the name Morvane Equity, or it could involve a symbol design that connotes "science" . We are open to ideas. We do not want alot of colors - but if any, color - blue is preferred. The font that seems to look best for the name (Morvane Equity) is arial black. We are open to ideas. Most important - we want to see a mock up of an actual business card with the logo concept embedded. The business card should include space for : company name, individual name, position title, cell phone, address. We hope to have this work done by Sept. 8.

Target Market(s)

We will be meeting with and giving the business card to institutions and high net worth individuals.

Industry/Entity Type

Investment Advisory

Contact Information for Business Card

Company name - Morvane Equity LLC
Individual name - Peter Dalby
Title - Portfolio Manager
Cell - (412) 555-0187
Address - 2650 Birchmont Lane, Suite 300, Atlanta GA 30327

Font styles to use
Other font styles liked:
• Arial

Colors
3277b5
0255a3
85acd3
cedeed
fdf9cf
d9d9d9
e6e6e6
f04a50
6b449b

Requirements
Must have
• Must have card details that are sited above.
• We would like a logo related to the name (Morvane Equity) or concept of the fund.
Nice to have
• We want conservative / understated / clean crisp look.
• If any colors - we prefer conservative appearance - blue / gray.
• I have enclosed an example of a card style that looks attractive - please do not exactly copy this card. This is not our company or logo. I feel the layout is attractive - just as an example
Should not have
• Avoid too much color.
• I have selected some preferred colors. Please do not use all of the colors - I have selected a few that might work - but I am not sure. We are open to your ideas so please do not feel the need to use all or any of these.

```html
<!DOCTYPE html>
<html lang="en">
<head>
<meta charset="utf-8">
<title>Morvane Equity – Business Card</title>
<link rel="stylesheet" href="https://fonts.googleapis.com/css2?family=Jost:wght@300;400;600;700&display=swap">
<style>
  :root {
    --page: #d9d9d9;
    --card-dark: #1c2430;
    --card-dark-hi: #2c3644;
    --accent-blue: #3277b5;
    --accent-blue-deep: #0255a3;
    --accent-blue-soft: #85acd3;
    --ink-white: #ffffff;
    --caption: #6a6f76;
  }
  * { margin: 0; padding: 0; box-sizing: border-box; }
  html, body { width: 1200px; height: 1200px; overflow: hidden; background: var(--page); }
  body { font-family: "Jost", "Futura", sans-serif; color: var(--ink-white); }
  .sheet {
    width: 1200px; height: 1200px;
    display: flex; flex-direction: column; align-items: center; justify-content: center; gap: 44px;
  }
  .card {
    position: relative; width: 840px; height: 480px; border-radius: 6px; overflow: hidden;
    box-shadow: 0 18px 40px rgba(0,0,0,.28);
  }
  .card svg.card-art { position: absolute; inset: 0; }
  .card-text { position: absolute; }

  /* front */
  .front .holder { left: 170px; top: 120px; }
  .front .holder-name { font-weight: 700; font-size: 108px; line-height: 1; letter-spacing: 1px; }
  .front .holder-title { font-weight: 300; font-size: 42px; letter-spacing: 1px; margin-top: 6px; margin-left: 6px; }
  .front .website { left: 40px; bottom: 30px; font-weight: 400; font-size: 38px; letter-spacing: 1px; }

  /* back */
  .back .firm { left: 60px; top: 120px; width: 350px; text-align: center; }
  .firm-mark { width: 46px; height: 46px; border-radius: 50%; background: var(--accent-blue); margin: 0 auto 16px; }
  .firm-name { font-weight: 700; font-size: 38px; letter-spacing: 1px; white-space: nowrap; }
  .firm-rule { display: flex; align-items: center; gap: 10px; margin-top: 6px; }
  .firm-rule .line { flex: 1; height: 1px; background: var(--ink-white); }
  .firm-rule .suffix { font-weight: 300; font-size: 18px; letter-spacing: 2px; }
  .back .holder { right: 36px; top: 60px; text-align: right; }
  .back .holder-name { font-weight: 700; font-size: 42px; line-height: 1.05; }
  .back .holder-title { font-weight: 400; font-size: 15px; letter-spacing: 1px; }
  .back .contact { right: 36px; bottom: 46px; text-align: right; font-weight: 600; font-size: 16px; letter-spacing: .5px; line-height: 1.55; }
  .back .contact .sub { font-size: 13px; }

  .caption { font-weight: 300; font-size: 15px; color: var(--caption); letter-spacing: .3px; margin-top: -26px; align-self: flex-end; margin-right: 180px; }
</style>
</head>
<body>
<main class="sheet">

  <section class="card front" aria-label="Card front">
    <svg class="card-art" width="840" height="480" viewBox="0 0 840 480">
      <defs>
        <radialGradient id="front-dark" cx="45%" cy="35%" r="70%">
          <stop offset="0" stop-color="var(--card-dark-hi)"/>
          <stop offset="1" stop-color="var(--card-dark)"/>
        </radialGradient>
        <linearGradient id="front-blue" x1="0" y1="0" x2="1" y2="0">
          <stop offset="0" stop-color="var(--accent-blue)"/>
          <stop offset="1" stop-color="var(--accent-blue-deep)"/>
        </linearGradient>
      </defs>
      <rect width="840" height="480" fill="url(#front-blue)"/>
      <path d="M0 0 H840 V372 H760 Q744 372 744 388 V396 Q744 412 728 412 H560 Q544 412 544 396 V388 Q544 372 528 372 H0 Z" fill="url(#front-dark)"/>
      <rect x="560" y="0" width="160" height="14" rx="7" fill="var(--accent-blue)"/>
    </svg>
    <div class="card-text holder">
      <div class="holder-name">Peter Dalby</div>
      <div class="holder-title">PORTFOLIO MANAGER</div>
    </div>
    <div class="card-text website">WWW.MORVANEEQUITY.COM</div>
  </section>

  <section class="card back" aria-label="Card back">
    <svg class="card-art" width="840" height="480" viewBox="0 0 840 480">
      <defs>
        <radialGradient id="back-dark" cx="40%" cy="45%" r="65%">
          <stop offset="0" stop-color="var(--card-dark-hi)"/>
          <stop offset="1" stop-color="var(--card-dark)"/>
        </radialGradient>
        <linearGradient id="back-blue" x1="0" y1="0" x2="1" y2="1">
          <stop offset="0" stop-color="var(--accent-blue)"/>
          <stop offset="1" stop-color="var(--accent-blue-deep)"/>
        </linearGradient>
      </defs>
      <rect width="840" height="480" fill="url(#back-blue)"/>
      <path d="M0 0 H440 V110 Q440 126 456 126 H464 Q480 126 480 142 V338 Q480 354 464 354 H456 Q440 354 440 370 V480 H0 Z" fill="url(#back-dark)"/>
      <rect x="70" y="-8" width="190" height="22" rx="9" fill="var(--accent-blue)"/>
    </svg>
    <div class="card-text firm">
      <div class="firm-mark"></div>
      <div class="firm-name">Morvane Equity</div>
      <div class="firm-rule"><span class="line"></span><span class="suffix">LLC</span><span class="line"></span></div>
    </div>
    <div class="card-text holder">
      <div class="holder-name">Peter Dalby</div>
      <div class="holder-title">PORTFOLIO MANAGER</div>
    </div>
    <div class="card-text contact">
      <div>CELL - (412) 555-0187</div>
      <div>ADDRESS - 2650 BIRCHMONT LANE</div>
      <div class="sub">SUITE 300, ATLANTA GA 30327</div>
    </div>
  </section>

  <p class="caption">2650 Birchmont Lane, Suite 300, Atlanta GA 30327</p>

</main>
</body>
</html>
```